I have a PHP web application to manage IT support calls and require a front-end design and user logon screen.

I have attached the current design which needs improving.

I have 2 current designs. The 2nd design is one I have been working on but requires a "professional touch". I also require the tables designed with dummy data from the 1st design.

I have attached my company logo in AI format which I would like incorporated into the design. There should also be a placeholder to supply the users company name upon login.

The screenshots I have attached should explain what I am looking for.

The Home Page should include charts which show statistical information such as:
Number of support tickets logged per month. Bar Chart etc.
Number of currently open support tickets.
Number of Quote Requests awaiting a response.
Number of Files and file repository.
Number of Reports.
Number of Customers.

For the Jobs and Customers pages the table fields should be designed as per the attached screenshots but a better looking tables. The table options such as uploading a file and adding a customer - these options can be changed and displayed differently.

Quotes page should display quotes returned and a "request a quote form".

Files page should have a good structure for browsing through an archive of files.

Profile page should have the option to include a profile picture.

An additional side page should be created for a web based calendar (these calendar entries will be updated by code).

The navbar should also include an alerts section.
The current attached design I have is based on bootstraps navbar.

Inspiration: http://plenvaro.com/freebie/free-admin-templates-for-backend-panels/

Hopefully this above link will show you some navigation style designs that I am looking for.

Please note, I will be doing the PHP coding myself and it is just the page designs I require in either HTML and or PHP format. I also require the CSS files for this project.
I need the code in a format where I can add and remove items in the menu from the code and not PSD/image based format.

If you think this project requires a higher budget let me know what you would expect and I will increase it!

Any questions, please let me know.
Dummy data can be shown for design purposes.

I have provided you a dummy login to our current system to show you the system:
https://reef.vomilbrixtonsolutions.co.uk/
username: dan.hollow@vomilbrixtonsolutions.co.uk
password:K#72zqTm

```html
<!DOCTYPE html>
<html lang="en">
<head>
<meta charset="utf-8">
<title>REEF – Jobs</title>
<link rel="stylesheet" href="https://fonts.googleapis.com/css2?family=Open+Sans:wght@300;400;600;700&display=swap">
<style>
  :root {
    --brand: #1f4a9c;
    --brand-dark: #18397a;
    --brand-text: #1f4a9c;
    --side-bg: #ffffff;
    --nav-bg: #ececec;
    --nav-line: #ffffff;
    --nav-text: #a9a9a9;
    --nav-icon: #c4c4c4;
    --page-bg: #f4f4f4;
    --band-bg: #efefef;
    --line: #dedede;
    --text: #555555;
    --muted: #8a8a8a;
    --soft: #b7b7b7;
    --badge: #e23b3b;
  }
  * { box-sizing: border-box; margin: 0; padding: 0; }
  html, body { width: 1200px; height: 675px; overflow: hidden; }
  body { font-family: "Open Sans", Arial, sans-serif; background: var(--page-bg); color: var(--text); position: relative; }

  .sidebar { position: absolute; left: 0; top: 0; width: 298px; height: 675px; background: var(--side-bg); box-shadow: 2px 0 4px rgba(0,0,0,.12); z-index: 3; }
  .brand { height: 119px; display: flex; align-items: center; padding-left: 16px; gap: 10px; }
  .brand-dot { width: 18px; height: 18px; border-radius: 50%; background: var(--brand); }
  .brand-name { font-size: 21px; font-weight: 600; color: var(--brand); letter-spacing: -.2px; }
  .nav { list-style: none; }
  .nav-item { height: 43px; background: var(--nav-bg); border-bottom: 1px solid var(--nav-line); display: flex; align-items: center; justify-content: space-between; padding: 0 18px 0 17px; font-size: 14px; color: var(--nav-text); }
  .nav-item svg { width: 24px; height: 24px; fill: none; stroke: var(--nav-icon); stroke-width: 1.8; }
  .nav-item.is-active { background: var(--brand); color: #fff; font-weight: 700; }
  .nav-item.is-active svg { stroke: #fff; }
  .side-foot { text-align: center; margin-top: 25px; font-size: 11px; color: #666; }
  .social { display: flex; justify-content: center; gap: 12px; margin-top: 14px; margin-left: -2px; }
  .social span { width: 26px; height: 26px; border-radius: 50%; background: #e2e2e2; }
  .social span:first-child { background: var(--brand); }

  .topbar { position: absolute; left: 298px; top: 0; right: 0; height: 54px; background: var(--brand); color: #fff; display: flex; align-items: center; }
  .app-name { margin-left: 22px; font-size: 16px; font-weight: 700; letter-spacing: .3px; }
  .app-sep { width: 1px; height: 30px; background: rgba(255,255,255,.3); margin: 0 10px 0 12px; }
  .app-title { font-size: 15px; }
  .top-actions { margin-left: auto; display: flex; height: 100%; align-items: center; font-size: 14px; }
  .alerts { position: relative; display: flex; align-items: center; gap: 5px; color: #c7d3ec; padding-right: 17px; }
  .alerts svg, .help svg, .user svg { width: 20px; height: 20px; }
  .badge { position: absolute; left: 58px; top: -14px; background: var(--badge); color: #fff; font-size: 10px; font-weight: 700; padding: 0 4px; border-radius: 2px; line-height: 14px; }
  .help { background: var(--brand-dark); height: 100%; width: 77px; display: flex; align-items: center; justify-content: center; gap: 4px; font-weight: 700; }
  .user { display: flex; align-items: center; gap: 6px; padding: 0 20px 0 16px; color: #c7d3ec; }

  .page-head { position: absolute; left: 298px; right: 0; top: 54px; height: 109px; background: #fff; box-shadow: 0 2px 4px rgba(0,0,0,.1); z-index: 2; }
  .page-title { position: absolute; left: 23px; bottom: 10px; font-size: 25px; font-weight: 600; color: var(--brand-text); display: flex; align-items: center; gap: 10px; }
  .page-title svg { width: 28px; height: 30px; fill: #d5d5d5; }
  .notch { position: absolute; left: 290px; top: 133px; width: 0; height: 0; border-top: 8px solid transparent; border-bottom: 8px solid transparent; border-right: 8px solid #fff; z-index: 4; }

  .panel-title { position: absolute; left: 321px; top: 192px; font-size: 14px; color: #555; }
  .pager { position: absolute; display: flex; }
  .pager span { width: 20px; height: 21px; background: #ececec; border: 1px solid #dcdcdc; display: flex; align-items: center; justify-content: center; }
  .pager span::after { content: ""; border-top: 3px solid transparent; border-bottom: 3px solid transparent; }
  .pager .prev::after { border-right: 4px solid #777; }
  .pager .next::after { border-left: 4px solid #777; }

  .jobs-table { position: absolute; left: 321px; top: 223px; width: 856px; border-collapse: collapse; background: #fff; font-size: 11px; text-align: center; }
  .jobs-table th, .jobs-table td { border: 1px solid var(--line); height: 34px; font-weight: 400; color: var(--muted); }
  .jobs-table th { height: 35px; font-weight: 600; color: #888; }
  .jobs-table .customer { color: var(--brand-text); font-weight: 600; }

  .recent { position: absolute; left: 298px; right: 0; top: 547px; bottom: 0; background: var(--band-bg); }
  .recent-title { position: absolute; left: 30px; top: 12px; font-size: 14px; color: #555; }
  .person { position: absolute; top: 46px; display: flex; align-items: center; gap: 16px; }
  .avatar { width: 59px; height: 59px; border-radius: 50%; }
  .person-name { font-size: 17.5px; font-weight: 300; color: #666; line-height: 1.3; }
  .person-country { font-size: 15px; font-weight: 300; color: var(--soft); }
</style>
</head>
<body>

<aside class="sidebar">
  <div class="brand"><span class="brand-dot"></span><span class="brand-name">Vomil Brixton</span></div>
  <ul class="nav">
    <li class="nav-item">Dashboard <svg viewBox="0 0 24 24"><path d="M3 17a9 9 0 0 1 18 0"/><path d="M12 17l4-5"/></svg></li>
    <li class="nav-item is-active">Jobs <svg viewBox="0 0 24 24"><path d="M12 3v18"/><path d="M4 8h15l2 2-2 2H4z"/></svg></li>
    <li class="nav-item">Customers <svg viewBox="0 0 24 24"><circle cx="10" cy="8" r="4"/><path d="M3 20c0-4 3-6 7-6s7 2 7 6"/></svg></li>
    <li class="nav-item">Inventory <svg viewBox="0 0 24 24"><path d="M4 8h16v12H4z"/><path d="M4 8l3-4h10l3 4"/></svg></li>
    <li class="nav-item">Reports <svg viewBox="0 0 24 24"><path d="M4 20V12M8 20V6M12 20V9M16 20V4M20 20v-7"/></svg></li>
    <li class="nav-item">Files <svg viewBox="0 0 24 24"><path d="M4 10h16v10H4z"/><path d="M6 10V5h12v5"/><path d="M9 15h6"/></svg></li>
    <li class="nav-item">Quotes <svg viewBox="0 0 24 24"><circle cx="10" cy="11" r="7"/><circle cx="17" cy="17" r="4"/></svg></li>
  </ul>
  <p class="side-foot">© &nbsp;Vomil Brixton Solutions. 2014</p>
  <div class="social"><span></span><span></span></div>
</aside>
<div class="notch"></div>

<header class="topbar">
  <span class="app-name">REEF</span>
  <span class="app-sep"></span>
  <span class="app-title">Call out and support tracker</span>
  <div class="top-actions">
    <div class="alerts">
      <svg viewBox="0 0 24 24" fill="none" stroke="currentColor" stroke-width="1.8"><circle cx="12" cy="12" r="9"/><path d="M13 6l-4 7h4l-2 5" /></svg>
      Alerts<span class="badge">11</span>
    </div>
    <div class="help">
      <svg viewBox="0 0 24 24" fill="none" stroke="#fff" stroke-width="2"><circle cx="12" cy="12" r="9"/><path d="M12 7v6M12 16v1"/></svg>
      Help
    </div>
    <div class="user">
      <svg viewBox="0 0 24 24" fill="currentColor"><circle cx="12" cy="8" r="4"/><path d="M4 21c0-5 4-7 8-7s8 2 8 7z"/></svg>
      Owen Harwick
      <svg viewBox="0 0 24 24" fill="currentColor" style="width:12px;height:12px"><path d="M4 8h16l-8 8z"/></svg>
    </div>
  </div>
</header>

<section class="page-head">
  <h1 class="page-title">Jobs
    <svg viewBox="0 0 28 30"><circle cx="12" cy="8" r="6"/><path d="M2 28c0-8 4-12 10-12 4 0 7 2 8 5v7z"/><path d="M20 20h2v3h3v2h-3v3h-2v-3h-3v-2h3z"/></svg>
  </h1>
</section>

<h2 class="panel-title" style="font-weight:400">Listing All Outstanding Jobs</h2>
<div class="pager" style="left:1136px;top:192px"><span class="prev"></span><span class="next"></span></div>

<table class="jobs-table">
  <colgroup><col style="width:116px"><col style="width:169px"><col style="width:293px"><col style="width:150px"><col></colgroup>
  <thead><tr><th>Job ID</th><th>Date &amp; Time</th><th>Customer</th><th>Subject</th><th>Actions</th></tr></thead>
  <tbody>
    <tr><td>15</td><td>2013-04-17 18:07:02</td><td class="customer">Peter Lane, Vomil Brixton Solutions Ltd</td><td>Subject</td><td>Close</td></tr>
    <tr><td>26</td><td>2014-04-24 14:01:35</td><td class="customer">Mary Cole, Vomil Brixton Solutions Ltd</td><td>test sub</td><td>Close</td></tr>
    <tr><td>15</td><td>2013-04-17 18:07:02</td><td class="customer">Peter Lane, Vomil Brixton Solutions Ltd</td><td>Testing</td><td>Close</td></tr>
    <tr><td>23</td><td>2013-04-17 18:07:02</td><td class="customer">Peter Lane, Vomil Brixton Solutions Ltd</td><td>Testing</td><td>Close</td></tr>
    <tr><td>42</td><td>2013-04-17 18:07:02</td><td class="customer">Peter Lane, Vomil Brixton Solutions Ltd</td><td>Testing</td><td>Close</td></tr>
    <tr><td>44</td><td>2013-04-17 18:07:02</td><td class="customer">Peter Lane, Vomil Brixton Solutions Ltd</td><td>Testing</td><td>Close</td></tr>
    <tr><td>34</td><td>2013-04-17 18:07:02</td><td class="customer">Peter Lane, Vomil Brixton Solutions Ltd</td><td>Testing</td><td>Close</td></tr>
  </tbody>
</table>

<section class="recent">
  <h2 class="recent-title" style="font-weight:400">Recent Customers</h2>
  <div class="pager" style="left:836px;top:10px"><span class="prev"></span><span class="next"></span></div>
  <div class="person" style="left:32px">
    <div class="avatar" role="img" aria-label="Customer profile photo" style="background:linear-gradient(135deg,#3a2a22,#c98f70)"></div>
    <div><div class="person-name">Elena Brook</div><div class="person-country">United Kingdom</div></div>
  </div>
  <div class="person" style="left:245px">
    <div class="avatar" role="img" aria-label="Customer avatar illustration" style="background:linear-gradient(135deg,#e0356a,#f2b0a0)"></div>
    <div><div class="person-name">Tobias Wren</div><div class="person-country">South Africa</div></div>
  </div>
  <div class="person" style="left:454px">
    <div class="avatar" role="img" aria-label="Customer profile photo" style="background:linear-gradient(135deg,#1d2a44,#6a7a9a)"></div>
    <div><div class="person-name">Marcus Dale</div><div class="person-country">United Kingdom</div></div>
  </div>
  <div class="person" style="left:669px">
    <div class="avatar" role="img" aria-label="Customer profile photo" style="background:linear-gradient(135deg,#8a7a66,#e4dccf)"></div>
    <div><div class="person-name">Felix Orton</div><div class="person-country">Australia</div></div>
  </div>
</section>

</body>
</html>
```